Brantley Advisory Group provides support for renewable energy projects to utilities and suppliers

I need a professional looking business card that is both simple and elegant and unique. My clients are mostly large organizations not individuals. I am a consultant with my own company that is small but would like to give clients the impression I am larger. Smart grid, fiber optics, software, field hardware, distribution automation, substation automation, operations, energy storage/batteries, microgrids, customer service, strategy/roadmaps, conservation, Automated Metering Infrastruture (AMI or smart meters) are all areas of focus.

Target Market(s)

Utilities, suppliers, governmental agencies involved in energy. All types of energy especially natural gas and electrical. Especially renewable energy or green projects.

Contact Information for Business Card

Name - Ross Brantley Cell Phone - 425.318.4762 Email - rbrantley@brantleyag-example.com
Company - Brantley Advisory Group (logo) Title - Principal

Font styles to use
Serif
Sans Serif

Colors

Designer to choose colors to be used in the design.

Requirements
Must have
• Simple and professional and powerful.
• Unique/creative design.
Nice to have
• Utilize color scheme to accent logo colors. Maybe some geometric pattern on edge of card with color.
Should not have
• Busy, complicated, traditional

```html
<!DOCTYPE html>
<html lang="en">
<head>
<meta charset="utf-8">
<title>Brantley Advisory Group – Business Card</title>
<link rel="stylesheet" href="https://fonts.googleapis.com/css2?family=Montserrat:wght@500;700&family=Lato:wght@400&display=swap">
<style>
  :root {
    --navy: #2b3595;
    --green: #5a8a35;
    --grey: #8c8c8c;
    --paper: #ffffff;
    --backdrop: #e3e3e8;
  }
  * { box-sizing: border-box; margin: 0; padding: 0; }
  html, body {
    width: 1200px;
    height: 900px;
    overflow: hidden;
    background: var(--backdrop);
  }
  .canvas {
    width: 1200px;
    height: 900px;
    display: flex;
    flex-direction: column;
    align-items: center;
    justify-content: center;
    gap: 60px;
  }
  .card {
    position: relative;
    width: 560px;
    height: 320px;
    background: var(--paper);
    box-shadow: 0 6px 18px rgba(40, 45, 80, 0.15);
    overflow: hidden;
  }

  /* Front side */
  .brand {
    position: absolute;
    top: 38px;
    left: 46px;
    display: flex;
    align-items: center;
    gap: 10px;
  }
  .brand-square {
    width: 18px;
    height: 18px;
    border: 2.5px solid var(--navy);
    border-radius: 3px;
  }
  .brand-name {
    font-family: "Montserrat", sans-serif;
    font-weight: 700;
    font-size: 17px;
    color: var(--navy);
    letter-spacing: 0.2px;
  }
  .person {
    position: absolute;
    top: 96px;
    left: 46px;
  }
  .person-name {
    font-family: "Montserrat", sans-serif;
    font-weight: 700;
    font-size: 30px;
    color: var(--navy);
    line-height: 1.1;
  }
  .person-title {
    font-family: "Lato", sans-serif;
    font-size: 14px;
    color: var(--green);
    letter-spacing: 0.6px;
    margin-top: 2px;
  }
  .contact {
    position: absolute;
    top: 188px;
    left: 46px;
    list-style: none;
    font-family: "Lato", sans-serif;
    font-size: 13px;
    color: var(--navy);
    letter-spacing: 0.5px;
  }
  .contact li {
    display: flex;
    align-items: center;
    gap: 12px;
    margin-bottom: 12px;
  }
  .contact svg { width: 16px; height: 16px; fill: var(--navy); flex: none; }
  .edge-pattern {
    position: absolute;
    right: 0;
    bottom: 0;
    width: 170px;
    height: 230px;
    background: linear-gradient(160deg, var(--navy) 0%, var(--green) 55%, var(--navy) 100%);
  }

  /* Back side */
  .card-back {
    display: flex;
    align-items: center;
    justify-content: center;
  }
  .card-back .brand {
    position: static;
    gap: 14px;
  }
  .card-back .brand-square { width: 26px; height: 26px; border-width: 3px; }
  .card-back .brand-name { font-size: 28px; }
</style>
</head>
<body>
<main class="canvas">
  <section class="card card-front">
    <div class="brand">
      <span class="brand-square"></span>
      <span class="brand-name">Brantley Advisory Group</span>
    </div>
    <div class="person">
      <h1 class="person-name">Ross Brantley</h1>
      <p class="person-title">Principal</p>
    </div>
    <ul class="contact">
      <li>
        <svg viewBox="0 0 24 24" aria-hidden="true"><path d="M6.6 10.8a15.1 15.1 0 0 0 6.6 6.6l2.2-2.2a1 1 0 0 1 1-.25 11.4 11.4 0 0 0 3.6.57 1 1 0 0 1 1 1V20a1 1 0 0 1-1 1A17 17 0 0 1 3 4a1 1 0 0 1 1-1h3.5a1 1 0 0 1 1 1c0 1.25.2 2.46.57 3.6a1 1 0 0 1-.25 1z"/></svg>
        <span>425.318.4762</span>
      </li>
      <li>
        <svg viewBox="0 0 24 24" aria-hidden="true"><path d="M2 5h20v14H2z M3.5 6.5 12 13l8.5-6.5" fill="none" stroke="#2b3595" stroke-width="2"/></svg>
        <span>rbrantley@brantleyag-example.com</span>
      </li>
    </ul>
    <div class="edge-pattern" role="img" aria-label="Geometric tile pattern in navy, green and grey along the card edge"></div>
  </section>

  <section class="card card-back">
    <div class="brand">
      <span class="brand-square"></span>
      <span class="brand-name">Brantley Advisory Group</span>
    </div>
  </section>
</main>
</body>
</html>
```